Wedding and event Photography company.

We need a business card design for a photography company based in Singapore named TamKeza. Our core service offering is wedding photojournalism. We would like to see minimalistic designs that use the colour white. The final design should communicate a sense of ease and reliability.

The attached are a couple of visual reference which i found over the web, i hope it will helps.

Project Brief Update (14th July 2014):
- Please refrain from using any images from the website for the design. The laws and regulations over here does not allow me to distribute my client's images. Thanks!

Target Market(s)

Young and middle aged adults aged 24 - 38. With money to spend =D

Industry/Entity Type

Business

Contact Information for Business Card

Name: Dev Lunor
Designation: Head Photographer
Mobile: +65 81749026
Email: jun@tamkeza.example
Website: www.tamkeza.example

Font styles to use
Other font styles liked:
• Baskerville URW

Colors

Designer to choose colors to be used in the design.

Requirements
Must have
• Must include:
• - The brand TamKeza
• - The logo attached
• - Please help to place the brand TamKeza with the logo according to your preferences.
• - Services
• - Wedding Photography
• - Portraiture
• - Photojournalism
Nice to have
• Looking forward to an elegant and simple design. Please see attached examples!
• Please use Serif Fonts
Should not have
• Please refrain from using dark tones for the majority of the design.
• Please refrain from letterpress and embossing.

```html
<!DOCTYPE html>
<html lang="en">
<head>
<meta charset="utf-8">
<title>TamKeza Business Card</title>
<link rel="stylesheet" href="https://fonts.googleapis.com/css2?family=Libre+Baskerville&display=swap">
<style>
  :root {
    --page-bg: #ece9e4;
    --sky-top: #a4b3c8;
    --sky-mid: #b6c2d2;
    --sky-low: #d3d9e1;
    --sky-base: #ecebe8;
    --ink-white: #ffffff;
    --brand-mist: #ebe8e3;
    --card-shadow: rgba(40, 40, 50, 0.28);
  }
  html, body {
    margin: 0;
    padding: 0;
    width: 1200px;
    height: 960px;
    overflow: hidden;
    background: var(--page-bg);
    font-family: "Libre Baskerville", "Baskerville", Georgia, serif;
  }
  .canvas {
    position: relative;
    width: 1200px;
    height: 960px;
  }
  .card {
    position: absolute;
    width: 600px;
    height: 342px;
    box-shadow: 1px 2px 4px var(--card-shadow);
    overflow: hidden;
  }
  .card--front { left: 314px; top: 114px; }
  .card--back  { left: 312px; top: 472px; height: 343px; }

  .card__sky {
    position: absolute;
    inset: 0;
    background: linear-gradient(180deg,
      var(--sky-top) 0%,
      var(--sky-mid) 40%,
      var(--sky-low) 72%,
      var(--sky-base) 100%);
  }
  .card__divider {
    position: absolute;
    width: 2px;
    background: var(--ink-white);
  }

  .holder-name {
    position: absolute;
    right: 324px;
    top: 148px;
    margin: 0;
    font-size: 29px;
    font-weight: 400;
    color: var(--ink-white);
    letter-spacing: -0.5px;
    white-space: nowrap;
  }
  .card--front .card__divider { left: 298px; top: 128px; height: 84px; }
  .contact-list {
    position: absolute;
    left: 320px;
    top: 139px;
    margin: 0;
    padding: 0;
    list-style: none;
    font-size: 13px;
    line-height: 19px;
    color: var(--ink-white);
  }

  .brand-name {
    position: absolute;
    right: 323px;
    top: 104px;
    margin: 0;
    font-size: 42px;
    font-weight: 400;
    color: var(--brand-mist);
    letter-spacing: -0.5px;
    white-space: nowrap;
  }
  .card--back .card__divider { left: 308px; top: 118px; height: 88px; }
  .service-list {
    position: absolute;
    left: 336px;
    top: 118px;
    margin: 0;
    padding: 0 0 0 18px;
    font-size: 14px;
    line-height: 30px;
    color: var(--ink-white);
  }
  .service-list li::marker { font-size: 12px; }
</style>
</head>
<body>
<main class="canvas">
  <section class="card card--front" aria-label="Business card front">
    <div class="card__sky" role="img" aria-label="Soft pale blue sky photograph with light clouds"></div>
    <h1 class="holder-name">Dev Lunor</h1>
    <div class="card__divider"></div>
    <ul class="contact-list">
      <li>+65 81749026</li>
      <li>jun@tamkeza.example</li>
      <li>www.tamkeza.example</li>
    </ul>
  </section>

  <section class="card card--back" aria-label="Business card back">
    <div class="card__sky" role="img" aria-label="Soft pale blue sky photograph with light clouds"></div>
    <h2 class="brand-name">TamKeza</h2>
    <div class="card__divider"></div>
    <ul class="service-list">
      <li>Wedding Photography</li>
      <li>Portraiture</li>
      <li>Photojournalism</li>
    </ul>
  </section>
</main>
</body>
</html>
```